3 x Professional Herbal Supplement Label Design Ready to Print in UK Standard + Example inc

Hi,
Thank you for taking the time to read. I'm looking for an excellent graphic designer experienced in creating supplement labels for our 3 new products. The labels should be sized and have the resolution ready for the printers.
Here is the work:
I'm looking for a new supplement label design that I can use for 3 new products called:
1 - Raspberry Ketone
2 - Garcinia Cambogia
3 - Green Coffee
You will only need to create a single label to enter the competition, as the label created will be the template for all 3 products listed above. You can choose whether you go for product 1, 2,or 3 to enter the design competition, but all 3 will be required on completion should you be selected.
Simply, the label template would be adjusted for the other products, what would be different is the product specifics like, name, background graphic of the ingredient and ingredients listed, directions of use, barcode etc.
The design I like, which I'd like you to copy and then artistically make different is attached and titled "CalderVital_Garcinia_Cambogia_LABEL.jpg"
My company logo is attached called "ulvix final logo.ai" & "ulvix-invis.png" - Please let me know if this resolution is not suitable.
The guidance information in designing a UK label from the supplement manufacturer is attached, as follows:
"Copy of Food supplement label template (2).xls"
The supplement manufacturer has also provided a very basic example of a product they produced for another company (Not very good I know, but at least shows what goes where). Please do not use this as an example of a good design!
"Soru-dex_label_3 - Copy.pdf"
*** I will provide more specific product detail (ingredients, bar-code, dosage) if your initial design is liked and selected for adjustment, as we will require that all 3 label designs are completed.
*** The delivered image files will need to be in Photoshop format.

```html
<!DOCTYPE html>
<html lang="en">
<head>
<meta charset="utf-8">
<title>ulvix Supplement Label Range</title>
<link rel="stylesheet" href="https://fonts.googleapis.com/css2?family=Michroma&family=Roboto:wght@300;400;700&display=swap">
<style>
  :root {
    --canvas: #ececec;
    --paper: #ffffff;
    --ink: #3a3a3a;
    --muted: #6a6a6a;
    --green-dark: #1e8a3e;
    --green-light: #4cb84a;
    --red-dark: #b8283a;
    --red-light: #de4a55;
    --orange-dark: #e8901a;
    --orange-light: #f7a823;
  }
  * { box-sizing: border-box; margin: 0; padding: 0; }
  html, body {
    width: 1200px; height: 709px; overflow: hidden;
    background: var(--canvas);
    font-family: "Roboto", Arial, sans-serif;
    color: var(--ink);
  }
  .range { position: relative; width: 1200px; height: 709px; }

  .label {
    position: absolute; left: 290px;
    width: 620px; height: 218px;
    background: var(--paper);
    border-radius: 12px;
    overflow: hidden;
    box-shadow: 0 1px 4px rgba(0,0,0,.18);
  }
  .label--coffee    { top: 12px;  --brand-dark: var(--green-dark);  --brand-light: var(--green-light); }
  .label--raspberry { top: 245px; --brand-dark: var(--red-dark);    --brand-light: var(--red-light); }
  .label--garcinia  { top: 478px; --brand-dark: var(--orange-dark); --brand-light: var(--orange-light); }

  .label__band { position: absolute; inset: 0; width: 620px; height: 218px; }

  .ingredients {
    position: absolute; left: 14px; top: 12px; width: 180px;
    font-size: 6.4px; line-height: 1.35; color: var(--ink);
  }
  .ingredients b { font-weight: 700; }
  .ingredients .note { margin-top: 5px; color: var(--brand-dark); font-weight: 700; }

  .directions {
    position: absolute; left: 466px; top: 12px; width: 144px;
    font-size: 6.4px; line-height: 1.35;
  }
  .directions p + p { margin-top: 5px; }

  .brand {
    position: absolute; left: 246px; top: 18px;
    display: flex; align-items: center; gap: 5px;
    font-size: 22px; font-weight: 400; color: var(--brand-dark);
    letter-spacing: .2px;
  }
  .brand__dot { width: 12px; height: 12px; border-radius: 50%; background: var(--brand-dark); }

  .capsules {
    position: absolute; left: 372px; top: 14px;
    font-size: 9px; line-height: 1.1; color: var(--brand-dark); font-weight: 300;
  }
  .capsules strong { display: block; font-size: 12px; font-weight: 400; margin-left: 22px; }

  .hero {
    position: absolute; left: 222px; top: 50px; width: 200px; height: 80px;
    border-radius: 50%;
  }
  .label--coffee .hero    { background: radial-gradient(ellipse at 50% 55%, #9ab85a 0%, #4f7d2c 55%, rgba(79,125,44,0) 75%); }
  .label--raspberry .hero { background: radial-gradient(ellipse at 50% 55%, #e2556b 0%, #b5283f 50%, rgba(181,40,63,0) 75%); }
  .label--garcinia .hero  { background: radial-gradient(ellipse at 50% 55%, #f2d33a 0%, #d9a41c 50%, rgba(217,164,28,0) 75%); }

  .facts {
    position: absolute; left: 14px; top: 120px; width: 170px; height: 82px;
    background: var(--paper); border: 1px solid #999;
    padding: 4px 5px; font-size: 6px; line-height: 1.4; color: var(--ink);
  }
  .facts h3 { font-size: 8px; font-weight: 700; border-bottom: 2px solid var(--ink); padding-bottom: 1px; margin-bottom: 2px; }
  .facts .row { border-bottom: 1px solid #bbb; display: flex; justify-content: space-between; }

  .product {
    position: absolute; left: 226px; top: 134px; width: 150px;
    color: #fff; text-align: center;
  }
  .product__name {
    font-family: "Michroma", "Arial Black", sans-serif;
    font-size: 19px; line-height: 1.12; text-transform: uppercase;
  }
  .product__name--wide { font-size: 14px; }
  .product__sub { font-size: 7px; letter-spacing: .4px; text-transform: uppercase; margin-top: 2px; }

  .claims {
    position: absolute; left: 384px; top: 138px; width: 70px;
    border-left: 1px solid rgba(255,255,255,.85);
    padding-left: 6px; color: #fff;
    font-size: 11px; font-weight: 300; line-height: 1.05;
  }
  .claims span { display: block; }
  .claims span + span { border-top: 1px solid rgba(255,255,255,.85); margin-top: 5px; padding-top: 5px; }

  .maker {
    position: absolute; left: 478px; top: 150px; color: #fff;
  }
  .maker__brand { display: flex; align-items: center; gap: 3px; font-size: 13px; font-weight: 400; }
  .maker__brand i { width: 7px; height: 7px; border-radius: 50%; background: #fff; display: inline-block; }
  .maker__details {
    position: absolute; left: 82px; top: -4px; width: 50px;
    font-size: 5.6px; line-height: 1.45; text-align: right;
  }
</style>
</head>
<body>
<main class="range">

  <!-- Green Coffee -->
  <article class="label label--coffee">
    <svg class="label__band" viewBox="0 0 620 218" aria-hidden="true">
      <defs>
        <linearGradient id="band-coffee" x1="0" x2="1" y1="0" y2="0">
          <stop offset="0" stop-color="#1e8a3e"/><stop offset="1" stop-color="#52bd4a"/>
        </linearGradient>
      </defs>
      <path d="M0 100 C150 80 250 132 400 112 S560 84 620 92 L620 218 L0 218 Z" fill="url(#band-coffee)"/>
      <path d="M0 108 C150 88 250 140 400 120 S560 92 620 100" fill="none" stroke="#fff" stroke-width="1.5" opacity=".7"/>
    </svg>
    <div class="ingredients">
      <p><b>Ingredients:</b> Whole herb extract, vegetarian capsule shell (hydroxypropyl methylcellulose), rice flour, anti-caking agent magnesium stearate.</p>
      <p class="note">Food supplements should not be used as a substitute for a varied diet.</p>
    </div>
    <div class="brand"><span class="brand__dot"></span>ulvix</div>
    <div class="capsules"><strong>120</strong>Vegetarian<br>Capsules</div>
    <div class="hero" role="img" aria-label="Green coffee beans with coffee leaves"></div>
    <div class="directions">
      <p><b>Directions for Use:</b> Take two capsules daily with water before a main meal. Do not exceed the recommended daily dose.</p>
      <p>Keep out of reach of young children. Store in a cool dry place.</p>
    </div>
    <div class="facts">
      <h3>Supplement Facts</h3>
      <div class="row"><span>Serving Size: 2 Capsules</span></div>
      <div class="row"><span>Servings Per Container: 60</span></div>
      <div class="row"><span>Amount per serving</span></div>
      <div class="row"><span>Active Extract</span><span>800mg</span></div>
    </div>
    <div class="product">
      <div class="product__name">Green<br>Coffee</div>
      <div class="product__sub">50% Chlorogenic Acid</div>
    </div>
    <div class="claims"><span>Advanced Formula</span><span>Maximum Strength</span></div>
    <div class="maker">
      <div class="maker__brand"><i></i>ulvix</div>
      <div class="maker__details">Company Name<br>Address<br>Country<br>Phone<br>Web</div>
    </div>
  </article>

  <!-- Raspberry Ketone -->
  <article class="label label--raspberry">
    <svg class="label__band" viewBox="0 0 620 218" aria-hidden="true">
      <defs>
        <linearGradient id="band-raspberry" x1="0" x2="1" y1="0" y2="0">
          <stop offset="0" stop-color="#b8283a"/><stop offset="1" stop-color="#e04e58"/>
        </linearGradient>
      </defs>
      <path d="M0 100 C150 80 250 132 400 112 S560 84 620 92 L620 218 L0 218 Z" fill="url(#band-raspberry)"/>
      <path d="M0 108 C150 88 250 140 400 120 S560 92 620 100" fill="none" stroke="#fff" stroke-width="1.5" opacity=".7"/>
    </svg>
    <div class="ingredients">
      <p><b>Ingredients:</b> Whole herb extract, vegetarian capsule shell (hydroxypropyl methylcellulose), rice flour, anti-caking agent magnesium stearate.</p>
      <p class="note">Food supplements should not be used as a substitute for a varied diet.</p>
    </div>
    <div class="brand"><span class="brand__dot"></span>ulvix</div>
    <div class="capsules"><strong>120</strong>Vegetarian<br>Capsules</div>
    <div class="hero" role="img" aria-label="Fresh raspberries with leaves"></div>
    <div class="directions">
      <p><b>Directions for Use:</b> Take two capsules daily with water before a main meal. Do not exceed the recommended daily dose.</p>
      <p>Keep out of reach of young children. Store in a cool dry place.</p>
    </div>
    <div class="facts">
      <h3>Supplement Facts</h3>
      <div class="row"><span>Serving Size: 2 Capsules</span></div>
      <div class="row"><span>Servings Per Container: 60</span></div>
      <div class="row"><span>Amount per serving</span></div>
      <div class="row"><span>Active Extract</span><span>800mg</span></div>
    </div>
    <div class="product">
      <div class="product__name"><span class="product__name--wide">Raspberry</span><br>Ketone</div>
      <div class="product__sub">Natural Raspberry Ketones</div>
    </div>
    <div class="claims"><span>Advanced Formula</span><span>Maximum Strength</span></div>
    <div class="maker">
      <div class="maker__brand"><i></i>ulvix</div>
      <div class="maker__details">Company Name<br>Address<br>Country<br>Phone<br>Web</div>
    </div>
  </article>

  <!-- Garcinia Cambogia -->
  <article class="label label--garcinia">
    <svg class="label__band" viewBox="0 0 620 218" aria-hidden="true">
      <defs>
        <linearGradient id="band-garcinia" x1="0" x2="1" y1="0" y2="0">
          <stop offset="0" stop-color="#e8901a"/><stop offset="1" stop-color="#f8ab26"/>
        </linearGradient>
      </defs>
      <path d="M0 100 C150 80 250 132 400 112 S560 84 620 92 L620 218 L0 218 Z" fill="url(#band-garcinia)"/>
      <path d="M0 108 C150 88 250 140 400 120 S560 92 620 100" fill="none" stroke="#fff" stroke-width="1.5" opacity=".7"/>
    </svg>
    <div class="ingredients">
      <p><b>Ingredients:</b> Whole herb extract, vegetarian capsule shell (hydroxypropyl methylcellulose), rice flour, anti-caking agent magnesium stearate.</p>
      <p class="note">Food supplements should not be used as a substitute for a varied diet.</p>
    </div>
    <div class="brand"><span class="brand__dot"></span>ulvix</div>
    <div class="capsules"><strong>120</strong>Vegetarian<br>Capsules</div>
    <div class="hero" role="img" aria-label="Ripe garcinia cambogia fruits"></div>
    <div class="directions">
      <p><b>Directions for Use:</b> Take two capsules daily with water before a main meal. Do not exceed the recommended daily dose.</p>
      <p>Keep out of reach of young children. Store in a cool dry place.</p>
    </div>
    <div class="facts">
      <h3>Supplement Facts</h3>
      <div class="row"><span>Serving Size: 2 Capsules</span></div>
      <div class="row"><span>Servings Per Container: 60</span></div>
      <div class="row"><span>Amount per serving</span></div>
      <div class="row"><span>Active Extract</span><span>800mg</span></div>
    </div>
    <div class="product">
      <div class="product__name"><span class="product__name--wide">Garcinia<br>Cambogia</span></div>
      <div class="product__sub">Whole Fruit Extract</div>
    </div>
    <div class="claims"><span>Advanced Formula</span><span>Maximum Strength</span></div>
    <div class="maker">
      <div class="maker__brand"><i></i>ulvix</div>
      <div class="maker__details">Company Name<br>Address<br>Country<br>Phone<br>Web</div>
    </div>
  </article>

</main>
</body>
</html>
```